Rack Card - Digital Marketing Course

I need a double sided rack card designed for a Digital Marketing Course I teach. http://www.tallpinestudios.ca/training is where the course details are.

Digital

```html
<!DOCTYPE html>
<html lang="en">
<head>
<meta charset="utf-8">
<title>Tall Pine Studios – Digital Marketing Course Rack Card</title>
<link href="https://fonts.googleapis.com/css2?family=Lato:wght@300;400;700&family=Roboto+Condensed:wght@400;700&family=Arimo:wght@700&display=swap" rel="stylesheet">
<style>
:root{
  --blue:#1565b8;
  --blue-dark:#0d4f99;
  --charcoal:#3a3d42;
  --gray-band:#c9cbce;
  --gray-light:#eceef0;
  --ink:#1f2124;
  --white:#ffffff;
}
*{box-sizing:border-box;margin:0;padding:0}
html,body{width:1200px;height:1200px;overflow:hidden;background:var(--white)}
body{position:relative;font-family:"Lato",sans-serif;color:var(--ink)}
.card{position:absolute;top:26px;width:527px;height:1116px;overflow:hidden;box-shadow:0 0 6px rgba(0,0,0,.35)}
.card--front{left:54px;background:linear-gradient(180deg,#fff 0%,#fff 48%,#e4e6e8 62%,#f3f4f5 76%,#d8dadd 100%)}
.card--back{left:614px;background:linear-gradient(180deg,#fff 0%,#fff 45%,#eef0f1 70%,#dcdee0 100%)}
.side-label{position:absolute;top:1144px;font-family:"Lato",sans-serif;font-size:31px;letter-spacing:2px;color:var(--ink)}
.side-label--front{left:280px}
.side-label--back{left:842px}
.abs{position:absolute}

/* brand */
.brand{position:absolute;display:flex;align-items:center;color:var(--blue)}
.brand__mark{background:var(--blue);flex:none}
.brand__name{font-family:"Lato",sans-serif;font-weight:400;line-height:1;color:var(--blue);white-space:nowrap}
.brand__name span{display:block}

/* front */
.front__brand{left:140px;top:51px}
.front__brand .brand__mark{width:74px;height:75px;margin-right:15px}
.front__brand .brand__name span:first-child{font-size:40px;letter-spacing:1px}
.front__brand .brand__name span:last-child{font-size:13px;letter-spacing:16px;margin-top:8px}
.front__art{left:0;top:150px}
.headline{left:34px;top:522px;width:480px;height:130px}
.headline__rule{position:absolute;left:0;top:6px;width:196px;height:6px;background:var(--blue)}
.headline__goal{position:absolute;left:2px;top:14px;font-family:"Roboto Condensed",sans-serif;font-size:35px;color:var(--ink);white-space:nowrap}
.headline__course{position:absolute;left:196px;top:-2px;font-family:"Roboto Condensed",sans-serif;font-weight:700;font-size:54px;color:var(--blue);border-bottom:4px solid var(--ink);line-height:1.02;padding-right:2px;white-space:nowrap}
.headline__develop{position:absolute;left:2px;top:62px;font-family:"Roboto Condensed",sans-serif;font-weight:700;font-size:48px;color:var(--blue);white-space:nowrap}
.headline__teams{position:absolute;right:0;top:64px;font-family:"Arimo",sans-serif;font-weight:700;font-size:29px;line-height:1;color:var(--ink);text-align:right;white-space:nowrap}
.headline__teams span{display:block;font-size:22px;margin-top:2px}

.section-band{position:absolute;left:0;height:36px;background:var(--gray-band)}
.section-band__pill{height:36px;background:var(--blue);color:var(--white);font-family:"Lato",sans-serif;font-size:23px;font-weight:400;line-height:36px;padding-left:22px;border-radius:0 18px 18px 0;white-space:nowrap}
.front__who{top:666px;width:527px}
.front__who .section-band__pill{width:283px;padding-left:26px}
.front__trainer{left:0;top:710px;width:214px;height:354px}
.trainer-text{left:222px;top:778px;width:293px;font-size:12.3px;line-height:15.6px;text-align:justify;color:#222}
.trainer-text p{margin-bottom:22px}
.front__footer-band{left:0;top:1064px;width:527px;height:52px;background:var(--blue)}
.front__footer{left:0;top:1076px;width:358px;height:40px;background:var(--charcoal);border-top:3px solid #fff;border-right:3px solid #fff;color:#fff;font-size:17px;letter-spacing:3.6px;line-height:36px;padding-left:32px;white-space:nowrap}

/* back */
.back__hero{left:0;top:0}
.back__brand{left:283px;top:287px}
.back__brand .brand__mark{width:47px;height:47px;margin-right:10px}
.back__brand .brand__name span:first-child{font-size:28px;letter-spacing:.5px}
.back__brand .brand__name span:last-child{font-size:9px;letter-spacing:11px;margin-top:5px}
.back__body{font-size:12.2px;line-height:18.6px;color:#222;text-align:justify}
.back__target-band{top:308px;width:206px}
.back__target-band .section-band__pill{width:188px}
.back__target-text{left:22px;top:360px;width:484px}
.back__target-text p{margin-bottom:11px}
.back__tech-band{top:502px;width:238px}
.back__tech-band .section-band__pill{width:222px}
.back__tech-text{left:22px;top:551px;width:219px}
.back__mkt-band{left:277px;top:503px;width:250px}
.back__mkt-band .section-band__pill{width:178px;padding-left:12px}
.back__mkt-text{left:278px;top:551px;width:228px}
.back__social-band{left:277px;top:716px;width:250px}
.back__social-band .section-band__pill{width:201px;margin-top:6px;padding-left:8px}
.back__social-text{left:281px;top:767px;width:225px}
.back__metrics-band{top:795px;width:238px}
.back__metrics-band .section-band__pill{width:187px}
.back__metrics-text{left:22px;top:841px;width:219px;text-align:left}
.badge{top:1059px;height:32px}
.badge--light{left:264px;width:126px;background:#fff;border:1px solid #d3d5d8}
.badge--dark{left:396px;width:97px;background:#2f3237}
.back__footer-band{left:0;top:1102px;width:527px;height:14px;background:var(--blue)}
.back__footer{left:0;top:1074px;width:260px;height:42px;background:var(--charcoal);clip-path:polygon(0 0,236px 0,260px 100%,0 100%);color:#fff;font-size:15.5px;line-height:40px;padding-left:37px;white-space:nowrap}
</style>
</head>
<body>

<!-- FRONT -->
<section class="card card--front">
  <div class="brand front__brand">
    <div class="brand__mark"></div>
    <div class="brand__name"><span>TALL PINE</span><span>STUDIOS</span></div>
  </div>

  <svg class="abs front__art" width="527" height="360" viewBox="0 150 527 360">
    <defs>
      <linearGradient id="portraitFill" x1="0" y1="0" x2="1" y2="1">
        <stop offset="0" stop-color="#e8edf2"/><stop offset="1" stop-color="#9fb6d0"/>
      </linearGradient>
      <radialGradient id="laptopFill" cx=".5" cy=".5" r=".6">
        <stop offset="0" stop-color="#f6f6f6"/><stop offset="1" stop-color="#cfd2d6"/>
      </radialGradient>
    </defs>
    <circle cx="394" cy="310" r="118" fill="var(--charcoal)"/>
    <circle cx="394" cy="310" r="108" fill="url(#laptopFill)" role="img" aria-label="Open laptop resting on a hand with app icons bursting from the screen"/>
    <circle cx="166" cy="318" r="156" fill="var(--blue)"/>
    <circle cx="166" cy="318" r="140" fill="url(#portraitFill)" role="img" aria-label="Portrait photo of a smiling businesswoman in a light blue shirt with arms crossed"/>
  </svg>

  <div class="abs headline">
    <div class="headline__rule"></div>
    <div class="headline__goal">THE GOAL OF</div>
    <div class="headline__course">THE COURSE</div>
    <div class="headline__develop">IS TO DEVELOP</div>
    <div class="headline__teams">your teams<span>marketing skills</span></div>
  </div>

  <div class="section-band front__who"><div class="section-band__pill">Who is the training for?</div></div>

  <div class="abs front__trainer" role="img" aria-label="Photo of the course instructor in a navy polo shirt with arms crossed" style="background:linear-gradient(180deg,#d7dade 0%,#2c3a55 45%,#1e2a40 100%)"></div>

  <div class="abs trainer-text">
    <p>The training is provided by Certified Relaywise Partner / Consultant &amp; Digital Marketing Certified Content Specialist Devin Marlowe. Both online &amp; live course components will be delivered by Devin.</p>
    <p>Devin is the Founder &amp; Head Marketing Strategist at Tall Pine Studios Inc. His experience includes both private, public &amp; non - profit businesses across Canada and the United States.</p>
    <p>As an entrepreneur since the age of 17, he brings lots of experience to each &amp; every client he works with.</p>
  </div>

  <div class="abs front__footer-band"></div>
  <div class="abs front__footer">www.tallpinestudios.ca</div>
</section>

<!-- BACK -->
<section class="card card--back">
  <svg class="abs back__hero" width="527" height="300" viewBox="0 0 527 300">
    <defs>
      <linearGradient id="deskFill" x1="0" y1="0" x2="1" y2="1">
        <stop offset="0" stop-color="#b08a63"/><stop offset=".5" stop-color="#d9dadb"/><stop offset="1" stop-color="#6f7378"/>
      </linearGradient>
    </defs>
    <ellipse cx="420" cy="-60" rx="708" ry="338" fill="var(--blue)"/>
    <ellipse cx="428" cy="-66" rx="700" ry="330" fill="var(--charcoal)"/>
    <ellipse cx="420" cy="-70" rx="690" ry="322" fill="url(#deskFill)" role="img" aria-label="Laptop on a desk showing marketing bar and pie charts, with a hand on the keyboard"/>
  </svg>

  <div class="brand back__brand">
    <div class="brand__mark"></div>
    <div class="brand__name"><span>TALL PINE</span><span>STUDIOS</span></div>
  </div>

  <div class="section-band back__target-band"><div class="section-band__pill">Your Target</div></div>
  <div class="abs back__body back__target-text">
    <p>Understanding your business &amp; how it currently fits into the marketing landscape is key. In this module, we will dive into key elements to understand cost per click, return in investment, key performance indicators, churn, segmentation &amp; retargeting.</p>
    <p>We will then craft your product offering, build out your ideal client profile &amp; outline the marketing that will need to be executed.</p>
  </div>

  <div class="section-band back__tech-band"><div class="section-band__pill">Your Technology</div></div>
  <div class="abs back__body back__tech-text">Relaywise will be the hub of your sales &amp; marketing efforts. This module take a deep dive into the essentials for learning, adapt &amp; understand, then apply &amp; master the software. In this module, we will learn to import your contacts, properly segment them in usable marketing format, integrate relaywise with you website &amp; other technology &amp; setup of 3 initial processes in automated campaign</div>

  <div class="section-band back__mkt-band"><div class="section-band__pill">Your Marketing</div></div>
  <div class="abs back__body back__mkt-text">Your team will work with us to learn &amp; develop marketing automation strategies to lead visitors on your website to take certain actions. In this module, we will learn to develop lead magnets, build nurture sequences &amp; sales conversion campaigns.</div>

  <div class="section-band back__social-band" style="background:linear-gradient(180deg,var(--gray-band) 0 36px,transparent 36px)"><div class="section-band__pill">Your Social Media</div></div>
  <div class="abs back__body back__social-text">Having a social media presence is a must for your business. This module focuses on the key 4 social media platforms ( Chatterbox, Pipline, Workfold &amp; Snapgrid ) to leverage your leads &amp; build trust with your audience. We will learn how to create engaging posts that create engagement, we will learn how to build a social marketing strategy that compliments your business objectives &amp; we will work together &amp; develop a social engagement process for your company.</div>

  <div class="section-band back__metrics-band"><div class="section-band__pill">Your Metrics</div></div>
  <div class="abs back__body back__metrics-text">Everything that you do in marketing is to gain a targeted &amp; measurable result. In this module we will learn how to distinguish key performance indicators (KPI) in your marketing efforts. We will create reporting widgets in your Relaywise application to report on campaign performance &amp; will learn how to meaningfully understand your social media insights and how they relate to your marketing efforts</div>

  <div class="abs badge badge--light"></div>
  <div class="abs badge badge--dark"></div>

  <div class="abs back__footer-band"></div>
  <div class="abs back__footer">www.tallpinestudios.ca</div>
</section>

<div class="side-label side-label--front">front</div>
<div class="side-label side-label--back">back</div>

</body>
</html>
```